Non-Fiction Book On Creativity - Cover Design / Physical and E-Book

I am looking for designs for my first book! It's called: Stillness Makes Harvest. The subtitle is: 27 Notes On Tending Gardens, Mending Fences, And Keeping A Patient Home.
It's a series of short lessons and principals on creativity and it will be a Kindle book and a physical book.
I'm really open to any type of designs but have attached some screenshots of other book covers that have a design and style that I like.
Please let me know if you have any questions or need any more information.
Creativity / Self-Help / Personal Development

```html
<!DOCTYPE html>
<html lang="en">
<head>
<meta charset="UTF-8">
<title>Stillness Makes Harvest — Book Cover</title>
<link rel="stylesheet" href="https://fonts.googleapis.com/css2?family=Barlow+Condensed:wght@500;600&family=Barlow+Semi+Condensed:wght@500&family=Libre+Baskerville&display=swap">
<style>
  :root {
    --backdrop: #b5b6b0;
    --paper: #ffffff;
    --navy: #0b3a60;
    --yellow: #fcee0a;
    --white: #ffffff;
    --ink: #1d1d1b;
    --bronze: #6b4a12;
    --art-tone-a: #f2f2ee;
    --art-tone-b: #e4e4dc;
  }
  * { margin: 0; padding: 0; box-sizing: border-box; }
  html, body {
    width: 1200px; height: 1000px; overflow: hidden;
    background: var(--backdrop);
  }
  .cover {
    position: absolute; left: 267px; top: 0;
    width: 666px; height: 1000px;
    background: var(--paper);
  }
  .cover-art {
    position: absolute; left: 150px; top: 12px;
    width: 440px; height: 321px;
    background: linear-gradient(180deg, var(--art-tone-a), var(--art-tone-b));
  }
  .title-band {
    position: absolute; left: 0; top: 333px;
    width: 666px; height: 470px;
    background: var(--navy);
    overflow: hidden;
  }
  .title-word {
    position: absolute; left: 88px; width: 493px;
    display: flex; justify-content: space-between;
    font-family: "Barlow Condensed", sans-serif;
    font-weight: 600; font-size: 92px; line-height: 1;
    color: var(--yellow);
  }
  .title-word--top { top: 18px; }
  .title-word--bottom { top: 354px; }
  .monogram {
    position: absolute; top: 62px;
    font-family: "Barlow Condensed", sans-serif;
    font-weight: 600; font-size: 318px; line-height: 1;
    color: var(--white);
  }
  .monogram--left { left: 96px; }
  .monogram--right { left: 450px; }
  .equals-bar {
    position: absolute; left: 260px; width: 159px; height: 22px;
    background: var(--white);
  }
  .equals-bar--top { top: 200px; }
  .equals-bar--bottom { top: 264px; }
  .connector-word {
    position: absolute; left: 260px; top: 234px; width: 159px;
    text-align: center;
    font-family: "Barlow Semi Condensed", sans-serif;
    font-weight: 500; font-size: 19px; letter-spacing: 2px; line-height: 1;
    color: var(--yellow);
  }
  .subtitle {
    position: absolute; left: 0; top: 812px; width: 666px;
    text-align: center;
    font-family: "Libre Baskerville", serif;
    font-size: 20px; line-height: 34px;
    color: var(--bronze);
  }
  .author {
    position: absolute; left: 0; top: 940px; width: 666px;
    text-align: center;
    font-family: "Barlow Semi Condensed", sans-serif;
    font-weight: 500; font-size: 25px; letter-spacing: 1.5px;
    color: var(--ink);
  }
</style>
</head>
<body>
  <main class="cover">
    <div class="cover-art" role="img" aria-label="Line illustration of a figure lifting an open head top while a yellow star idea pops out"></div>

    <section class="title-band">
      <h1 aria-label="Stillness Makes Harvest">
        <span class="title-word title-word--top" aria-hidden="true"><span>S</span><span>T</span><span>I</span><span>L</span><span>L</span><span>N</span><span>E</span><span>S</span><span>S</span></span>
        <span class="monogram monogram--left" aria-hidden="true">S</span>
        <span class="equals-bar equals-bar--top" aria-hidden="true"></span>
        <span class="connector-word" aria-hidden="true">MAKES</span>
        <span class="equals-bar equals-bar--bottom" aria-hidden="true"></span>
        <span class="monogram monogram--right" aria-hidden="true">H</span>
        <span class="title-word title-word--bottom" aria-hidden="true"><span>H</span><span>A</span><span>R</span><span>V</span><span>E</span><span>S</span><span>T</span></span>
      </h1>
    </section>

    <p class="subtitle">27 Notes On Tending Gardens,<br>Mending Fences,<br>And Keeping A Patient Home.</p>

    <p class="author">AUTHOR’S NAME</p>
  </main>
</body>
</html>
```